Legal Stationary

A full set of stationery is required
The image and logo, along with colour, are set and attached.
The style should be modern, clean, and corporate. Not just a basic template off the web.
In addition to the address/website/email/phone fields for DX and KWT number, with the text “the firm is authorised and regulated by the KWT”
All files in all formats will be needed to allow editing after. Initial setup of templates will be required, and details for 4 business cards will be supplied.
Target Market(s)
Consumers of legal services
Industry/Entity Type
Legal

```html
<!DOCTYPE html>
<html lang="en">
<head>
<meta charset="utf-8">
<title>Marlow Law — Stationery Set</title>
<link href="https://fonts.googleapis.com/css2?family=Montserrat:wght@400;500;600;700&family=Lato:wght@400;700&display=swap" rel="stylesheet">
<style>
  :root{
    --bg:#d3d4d6;
    --paper:#ffffff;
    --brand:#283b91;
    --ink:#111111;
    --muted:#6b6b6b;
    --body:#7a7a7a;
  }
  *{box-sizing:border-box;margin:0;padding:0}
  html,body{width:1200px;height:1008px;overflow:hidden;background:var(--bg)}
  body{position:relative;font-family:"Lato",sans-serif;color:var(--ink)}
  .sheet{position:absolute;background:var(--paper);overflow:hidden}
  .brand-name{font-family:"Montserrat",sans-serif;font-weight:600;color:var(--brand);white-space:nowrap;letter-spacing:.3px;line-height:1}
  .brand-name.on-dark{color:#fff}
  .stripe{position:absolute;left:0;width:100%}
  .contact{list-style:none;font-family:"Montserrat",sans-serif;color:var(--muted)}
  .contact li{display:flex;align-items:flex-start;gap:4px}
  .contact svg{flex:none;fill:var(--ink)}
  .person{font-family:"Montserrat",sans-serif;color:var(--brand);font-weight:500;line-height:1.1;white-space:nowrap}
  .person b{font-weight:700}
  .role{font-family:"Montserrat",sans-serif;color:var(--muted)}
  .rule{background:var(--muted);height:1px}

  /* business card front */
  .card-front{left:109px;top:105px;width:249px;height:150px}
  .card-front .brand-name{position:absolute;left:25px;top:66px;font-size:12px}
  .card-front .details{position:absolute;left:136px;top:34px}
  .card-front .person{font-size:7.5px}
  .card-front .role{font-size:5.8px;margin-top:1px}
  .card-front .rule{width:21px;margin:4px 0 8px}
  .card-front .contact{font-size:5.3px;line-height:1.25}
  .card-front .contact li{margin-bottom:4.5px}

  /* business card back */
  .card-back{left:109px;top:298px;width:249px;height:149px;background:var(--brand);display:flex;align-items:center;justify-content:center}
  .card-back .brand-name{font-size:16px}

  /* letterhead */
  .letterhead{left:408px;top:72px;width:299px;height:419px}
  .letterhead .brand-name{position:absolute;left:22px;top:34px;font-size:10.6px}
  .letterhead .contact{position:absolute;left:219px;top:19px;font-size:4.1px;line-height:1.2}
  .letterhead .contact li{margin-bottom:3px}
  .recipient{position:absolute;left:24px;top:86px;font-family:"Montserrat",sans-serif}
  .recipient .to{font-size:5px;color:var(--muted)}
  .recipient h2{font-size:8.4px;font-weight:700;color:var(--brand);margin:1px 0 6px}
  .recipient dl{font-size:5.3px;color:var(--muted);line-height:1.3}
  .recipient dt{display:inline;color:var(--brand);font-weight:600}
  .recipient dd{display:inline;margin:0}
  .recipient .row{margin-bottom:3px}
  .letter-date{position:absolute;right:24px;top:146px;font-family:"Montserrat",sans-serif;font-size:5.6px;color:var(--muted)}
  .letter-body{position:absolute;left:24px;top:161px;width:251px;font-size:6.7px;line-height:9.8px;color:var(--body);text-align:justify}
  .letter-body p{margin-bottom:9.8px}
  .signoff{position:absolute;left:24px;top:327px;font-family:"Montserrat",sans-serif;font-size:6.6px;font-weight:600}
  .signature{position:absolute;left:38px;top:340px;width:50px;height:28px;background:linear-gradient(90deg,#f1f1f1,#e6e6e6)}

  /* compliments slip */
  .slip{left:747px;top:86px;width:355px;height:90px}
  .slip .brand-name{position:absolute;left:11px;top:39px;font-size:9.6px}
  .slip .details{position:absolute;left:98px;top:15px}
  .slip .person{font-size:6px}
  .slip .role{font-size:4.6px}
  .slip .rule{width:16px;margin:3px 0 5px}
  .slip .contact{font-size:4.1px;line-height:1.2}
  .slip .contact li{margin-bottom:3px}

  /* notebook cover */
  .notebook{left:779px;top:218px;width:310px;height:437px}
  .notebook .brand-name{position:absolute;left:0;right:0;top:208px;text-align:center;font-size:20px}
  .notebook .web{position:absolute;left:0;right:0;top:398px;text-align:center;font-family:"Montserrat",sans-serif;font-size:6.6px;font-weight:600;letter-spacing:1px}
  .notebook .web span{color:var(--brand)}

  /* presentation folder */
  .folder{position:absolute;left:96px;top:529px;width:610px;height:436px}
  .folder .brand-name{position:absolute}
  .folder .back-name{left:87px;top:295px;width:261px;text-align:center;font-size:10px}
  .folder .front-name{left:348px;top:166px;width:262px;text-align:center;font-size:15px}
  .folder .back-contact{position:absolute;left:87px;top:318px;width:261px;display:flex;justify-content:center;gap:6px;font-family:"Montserrat",sans-serif;font-size:5px;color:#fff}
  .folder .back-contact span{display:flex;align-items:center;gap:2px}
  .folder .back-contact svg{fill:#fff}

  /* envelope */
  .envelope{left:762px;top:711px;width:351px;height:165px}
  .envelope .brand-name{position:absolute;left:15px;top:19px;font-size:10px}
  .envelope .window{position:absolute;left:234px;top:94px;width:85px;height:34px;border-radius:3px;background:linear-gradient(135deg,#e3e3e3,#f3f3f3 50%,#dcdcdc);border:1px solid #d0d0d0}
  .envelope .footer-address{position:absolute;left:13px;top:145px;font-family:"Montserrat",sans-serif;font-size:3.8px;line-height:5px;color:var(--muted);display:flex;align-items:center;gap:2px;background:#fff;padding-right:2px;z-index:1}
</style>
</head>
<body>

<svg width="0" height="0" style="position:absolute">
  <defs>
    <symbol id="icon-pin" viewBox="0 0 10 10"><rect width="10" height="10" rx="1.5"/><path d="M5 2a2.2 2.2 0 0 0-2.2 2.2C2.8 5.9 5 8 5 8s2.2-2.1 2.2-3.8A2.2 2.2 0 0 0 5 2zm0 3a.8.8 0 1 1 0-1.6.8.8 0 0 1 0 1.6z" fill="#fff"/></symbol>
    <symbol id="icon-phone" viewBox="0 0 10 10"><rect width="10" height="10" rx="1.5"/><path d="M3.2 2.2l1 1.6-.6.7c.4.9 1 1.5 1.9 1.9l.7-.6 1.6 1-.5 1.1C5 7.8 2.2 5 2.1 2.7z" fill="#fff"/></symbol>
    <symbol id="icon-mail" viewBox="0 0 10 10"><rect width="10" height="10" rx="1.5"/><rect x="2" y="3" width="6" height="4" fill="#fff"/><path d="M2 3l3 2.3L8 3" stroke="#111" stroke-width=".6" fill="none"/></symbol>
    <symbol id="icon-web" viewBox="0 0 10 10"><rect width="10" height="10" rx="1.5"/><path d="M3.5 2.5v5l1.3-1.2 1 2 .8-.4-1-2H7.3z" fill="#fff"/></symbol>
  </defs>
</svg>

<!-- Business card, front -->
<section class="sheet card-front" aria-label="Business card front">
  <div class="brand-name">MARLOW LAW</div>
  <div class="details">
    <div class="person">DANIEL P. <b>MORROW</b></div>
    <div class="role">Managing Director</div>
    <div class="rule"></div>
    <ul class="contact">
      <li><svg width="7" height="7"><use href="#icon-pin"/></svg><span>210 Harbor Crescent<br>Arlington, VA 22201</span></li>
      <li><svg width="7" height="7"><use href="#icon-phone"/></svg><span>+00 123 456 78</span></li>
      <li><svg width="7" height="7"><use href="#icon-mail"/></svg><span>office@marlowlaw.com</span></li>
      <li><svg width="7" height="7"><use href="#icon-web"/></svg><span>www.marlowlaw.com</span></li>
    </ul>
  </div>
  <svg class="stripe" style="top:128px" width="249" height="6" viewBox="0 0 249 6">
    <rect x="0" y="1.5" width="124" height="1.6" fill="var(--ink)"/>
    <polygon points="127,0 249,0 249,4 123,4" fill="var(--brand)"/>
  </svg>
</section>

<!-- Business card, back -->
<section class="sheet card-back" aria-label="Business card back">
  <div class="brand-name on-dark">MARLOW LAW</div>
</section>

<!-- Letterhead -->
<section class="sheet letterhead" aria-label="Letterhead">
  <div class="brand-name">MARLOW LAW</div>
  <ul class="contact">
    <li><svg width="5.5" height="5.5"><use href="#icon-pin"/></svg><span>210 Harbor Crescent<br>Arlington, VA 22201</span></li>
    <li><svg width="5.5" height="5.5"><use href="#icon-phone"/></svg><span>+00 123 456 78</span></li>
    <li><svg width="5.5" height="5.5"><use href="#icon-mail"/></svg><span>office@marlowlaw.com</span></li>
    <li><svg width="5.5" height="5.5"><use href="#icon-web"/></svg><span>www.marlowlaw.com</span></li>
  </ul>
  <div class="recipient">
    <div class="to">To</div>
    <h2>CLARA HENSLEY</h2>
    <dl>
      <div class="row"><dt>A : </dt><dd>1234 City Your Ln. Suite 123<br>&nbsp;&nbsp;&nbsp;&nbsp;Dallas, TX 0000</dd></div>
      <div class="row"><dt>P : </dt><dd>0123-456-789</dd></div>
      <div class="row"><dt>E : </dt><dd>info@youremailaddress.com</dd></div>
    </dl>
  </div>
  <div class="letter-date">12 December, 2024</div>
  <div class="letter-body">
    <p>Lorem ipsum dolor sit amet, consectetuer adipiscing elit, sed diam nonummy nibh euismod tincidunt ut laoreet dolore magna aliquam erat volutpat. Ut wisi enim ad minim veniam, quis nostrud exerci tation ullamcorper suscipit lobortis nisl ut aliquip ex ea commodo consequat. Duis autem vel eum iriure dolor in hendrerit in vulputate velit esse molestie consequat, vel illum dolore eu feugiat nulla facilisis at vero eros et accumsan et iusto odio dignissim qui blandit praesent luptatum zzril delenit augue duis dolore te feugait nulla facilisi.</p>
    <p>Lorem ipsum dolor sit amet, cons ectetuer adipiscing elit, sed diam nonummy nibh euismod tincidunt ut laoreet dolore magna aliquam erat volutpat. Ut wisi enim ad minim veniam, quis nostrud exerci tation ullamcorper suscipit lobortis nisl ut aliquip ex ea commodo consequat.</p>
    <p>Lorem ipsum dolor sit amet, consectetuer adipiscing elit, sed diam nonummy nibh euismod tincidunt ut laoreet dolore magna aliquam erat</p>
  </div>
  <div class="signoff">Mr. Daniel P. Morrow</div>
  <div class="signature" role="img" aria-label="Handwritten signature"></div>
  <svg class="stripe" style="top:396px" width="299" height="8" viewBox="0 0 299 8">
    <rect x="0" y="3" width="195" height="3" fill="var(--ink)"/>
    <polygon points="202,0 299,0 299,6 196,6" fill="var(--brand)"/>
  </svg>
</section>

<!-- Compliments slip -->
<section class="sheet slip" aria-label="Compliments slip">
  <div class="brand-name">MARLOW LAW</div>
  <div class="details">
    <div class="person">DANIEL P. <b>MORROW</b></div>
    <div class="role">Managing Director</div>
    <div class="rule"></div>
    <ul class="contact">
      <li><svg width="5.5" height="5.5"><use href="#icon-pin"/></svg><span>210 Harbor Crescent<br>Arlington, VA 22201</span></li>
      <li><svg width="5.5" height="5.5"><use href="#icon-phone"/></svg><span>+00 123 456 78</span></li>
      <li><svg width="5.5" height="5.5"><use href="#icon-mail"/></svg><span>office@marlowlaw.com</span></li>
      <li><svg width="5.5" height="5.5"><use href="#icon-web"/></svg><span>www.marlowlaw.com</span></li>
    </ul>
  </div>
  <svg class="stripe" style="top:78px" width="355" height="5" viewBox="0 0 355 5">
    <rect x="0" y="1.5" width="198" height="1.6" fill="var(--ink)"/>
    <polygon points="201,0 355,0 355,3 198,3" fill="var(--brand)"/>
  </svg>
</section>

<!-- Notebook cover -->
<section class="sheet notebook" aria-label="Notebook cover">
  <svg class="stripe" style="top:14px" width="310" height="6" viewBox="0 0 310 6">
    <polygon points="0,0 110,0 104,6 0,6" fill="var(--brand)"/>
    <rect x="109" y="0" width="201" height="3" fill="var(--ink)"/>
  </svg>
  <div class="brand-name">MARLOW LAW</div>
  <div class="web">www.<span>marlowlaw</span>.com</div>
  <svg class="stripe" style="top:414px" width="310" height="7" viewBox="0 0 310 7">
    <rect x="0" y="3" width="200" height="3" fill="var(--ink)"/>
    <polygon points="207,0 310,0 310,6 201,6" fill="var(--brand)"/>
  </svg>
</section>

<!-- Presentation folder (unfolded) -->
<section class="folder" aria-label="Presentation folder">
  <svg width="610" height="436" viewBox="0 0 610 436">
    <path d="M87 0 L25 11 Q0 17 0 40 L0 302 Q0 323 25 327 L87 348 Z" fill="var(--paper)"/>
    <path d="M87 348 L348 348 L338 412 Q332 436 305 436 L130 436 Q104 436 98 412 Z" fill="var(--paper)"/>
    <rect x="87" y="0" width="261" height="348" fill="var(--brand)"/>
    <rect x="348" y="0" width="262" height="348" fill="var(--paper)"/>
    <polygon points="348,13 434,13 430,19 348,19" fill="var(--brand)"/>
    <rect x="433" y="14" width="177" height="2.5" fill="var(--ink)"/>
    <rect x="348" y="330" width="156" height="2.5" fill="var(--ink)"/>
    <polygon points="507,328 610,328 610,334 503,334" fill="var(--brand)"/>
  </svg>
  <div class="brand-name on-dark back-name">MARLOW LAW</div>
  <div class="back-contact">
    <span><svg width="5" height="5" viewBox="0 0 10 10"><path d="M2 1l2 3-1 1.3c.8 1.6 2 2.8 3.6 3.6L8 8l2 1.5-1 .5C5 10 0 5 .5 1z"/></svg>+00 123 456 78</span>
    <span><svg width="5" height="5" viewBox="0 0 10 10"><rect x="0" y="2" width="10" height="6"/></svg>office@marlowlaw.com</span>
    <span><svg width="5" height="5" viewBox="0 0 10 10"><circle cx="5" cy="5" r="4.2" fill="none" stroke="#fff" stroke-width="1.5"/></svg>www.marlowlaw.com</span>
  </div>
  <div class="brand-name front-name">MARLOW LAW</div>
</section>

<!-- Envelope -->
<section class="sheet envelope" aria-label="Window envelope">
  <div class="brand-name">MARLOW LAW</div>
  <div class="window"></div>
  <div class="footer-address"><svg width="5" height="5" style="fill:var(--ink)"><use href="#icon-pin"/></svg>210 Harbor Crescent Arlington, VA 22201</div>
  <svg class="stripe" style="top:146px" width="351" height="5" viewBox="0 0 351 5">
    <rect x="0" y="1.5" width="210" height="1.3" fill="var(--ink)"/>
    <polygon points="213,0 351,0 351,4 209,4" fill="var(--brand)"/>
  </svg>
</section>

</body>
</html>
```